Pet business needs a business card

Pet shop needs a business card. Like dark background and and debased look.

Meadowpaws
Lindenweg 47
B - 3280 Velmor
Belgium

www.meadowpaws-example.com
mail@meadowpaws-example.com
Phone +32478610927

I will ad a tagline shortly.

Industry/Entity Type

Shop

Font styles to use
Sans Serif

Requirements
Must have
• Must be possible to print the card debased. See example image.

```html
<!DOCTYPE html>
<html lang="en">
<head>
<meta charset="utf-8">
<title>Meadowpaws – Business Card</title>
<link rel="stylesheet" href="https://fonts.googleapis.com/css2?family=Josefin+Sans:wght@300;400&display=swap">
<style>
  :root {
    --page: #ffffff;
    --card-yellow: #e6e01a;
    --card-yellow-deep: #dcd512;
    --card-grey: #e3e3e3;
    --band-orange: #f8a54b;
    --ink: #111111;
    --mark-grey: #6e6b5e;
    --mark-orange: #f5a043;
    --disc-white: #ffffff;
    --disc-rim: #77736a;
  }
  * { box-sizing: border-box; margin: 0; padding: 0; }
  html, body {
    width: 1000px;
    height: 1200px;
    overflow: hidden;
    background: var(--page);
    font-family: "Josefin Sans", sans-serif;
    color: var(--ink);
  }
  .canvas {
    position: relative;
    width: 1000px;
    height: 1200px;
  }

  /* Front face */
  .card-front {
    position: absolute;
    left: 37px;
    top: 82px;
    width: 901px;
    height: 518px;
    background: var(--card-yellow);
    overflow: hidden;
  }
  .card-front__texture {
    position: absolute;
    inset: 0;
    background:
      radial-gradient(circle at 14% 30%, rgba(200, 190, 20, 0.35) 0, rgba(200, 190, 20, 0) 22%),
      radial-gradient(circle at 20% 85%, rgba(200, 190, 20, 0.3) 0, rgba(200, 190, 20, 0) 20%),
      linear-gradient(180deg, var(--card-yellow) 0%, var(--card-yellow-deep) 100%);
  }
  .card-front__brand {
    position: absolute;
    left: 0;
    right: 0;
    top: 300px;
    display: flex;
    justify-content: center;
    align-items: center;
    gap: 22px;
  }
  .brand-dot {
    width: 34px;
    height: 34px;
    border-radius: 50%;
    background: var(--mark-orange);
  }
  .brand-name {
    font-family: "Josefin Sans", sans-serif;
    font-weight: 400;
    font-size: 72px;
    line-height: 1;
    color: var(--mark-grey);
    letter-spacing: 1px;
    padding-top: 8px;
  }

  /* Back face */
  .card-back {
    position: absolute;
    left: 34px;
    top: 645px;
    width: 902px;
    height: 511px;
    background: var(--card-grey);
  }
  .card-back__band {
    position: absolute;
    left: 123px;
    top: 0;
    width: 396px;
    height: 511px;
    background: var(--band-orange);
    text-align: center;
  }
  .company {
    margin-top: 78px;
    font-weight: 300;
    font-size: 50px;
    line-height: 1;
  }
  .address {
    margin-top: 18px;
    font-weight: 300;
    font-size: 31px;
    line-height: 52px;
  }
  .contact {
    margin-top: 22px;
    font-weight: 300;
    font-size: 22px;
    line-height: 40px;
  }
  .card-back__disc {
    position: absolute;
    left: 560px;
    top: 98px;
    width: 308px;
    height: 304px;
    border-radius: 50%;
    background: var(--disc-white);
    border: 3px solid var(--disc-rim);
    display: flex;
    align-items: center;
    justify-content: center;
  }
  .disc-name {
    font-family: "Josefin Sans", sans-serif;
    font-weight: 400;
    font-size: 40px;
    line-height: 1;
    color: var(--mark-orange);
    padding-top: 6px;
  }
</style>
</head>
<body>
<main class="canvas">
  <section class="card-front">
    <div class="card-front__texture" role="img" aria-label="Faint floral mandala texture over a yellow card background"></div>
    <div class="card-front__brand">
      <span class="brand-dot"></span>
      <span class="brand-name">Meadowpaws</span>
    </div>
  </section>

  <section class="card-back">
    <div class="card-back__band">
      <h1 class="company">Meadowpaws</h1>
      <p class="address">Lindenweg 47<br>B-3280 Velmor<br>Belgium</p>
      <p class="contact">www.meadowpaws-example.com<br>mail@meadowpaws-example.com<br>phone no: +32478610927</p>
    </div>
    <div class="card-back__disc">
      <span class="disc-name">Meadowpaws</span>
    </div>
  </section>
</main>
</body>
</html>
```